Environmentally conscious Waste Management Company requires business card

We Require a Business card for our environmentally conscious waste management company . The business card should have a very clean design. be double sided and incorporate our logo..
The card will need o have 9 lines for the contact details - that are
Name
Title
Business
Address Line 1
Address Line 2
Address Line 3
Phone
Mobile
Email

Industry/Entity Type

Waste Management

Other font styles liked:
• Helvetica or similar

```html
<!DOCTYPE html>
<html lang="en">
<head>
<meta charset="utf-8">
<title>Brightbins – Business Card</title>
<link href="https://fonts.googleapis.com/css2?family=Open+Sans:wght@400;600&display=swap" rel="stylesheet">
<style>
  :root {
    --green: #2fa33b;
    --green-dark: #1f8f2c;
    --green-light: #7fd58a;
    --ink: #4a4a4a;
    --paper: #ffffff;
    --backdrop: #ecedea;
    --rule: #8fd298;
  }
  * { box-sizing: border-box; margin: 0; padding: 0; }
  html, body { width: 1200px; height: 900px; overflow: hidden; }
  body {
    background: var(--backdrop);
    font-family: "Open Sans", Helvetica, Arial, sans-serif;
    position: relative;
  }
  .card {
    position: absolute;
    left: 290px;
    width: 620px;
    height: 354px;
    background: var(--paper);
    overflow: hidden;
    box-shadow: 0 6px 18px rgba(0,0,0,0.12);
  }
  .card--front { top: 70px; }
  .card--back { top: 476px; }

  /* Front */
  .front-band {
    position: absolute;
    left: 0; top: 0; right: 0;
    height: 150px;
    background: linear-gradient(160deg, var(--green-light) 0%, var(--green) 60%, var(--green-dark) 100%);
  }
  .brand {
    position: absolute;
    color: var(--green);
    font-weight: 400;
    line-height: 1;
    white-space: nowrap;
  }
  .card--front .brand { left: 44px; top: 196px; font-size: 64px; }

  /* Back */
  .card--back .brand { left: 40px; top: 156px; font-size: 34px; }
  .divider {
    position: absolute;
    left: 322px; top: 62px;
    width: 1px; height: 230px;
    background: var(--rule);
  }
  .contact {
    position: absolute;
    left: 346px; top: 58px;
    font-size: 13px;
    line-height: 1.35;
    color: var(--green);
  }
  .contact__name {
    color: var(--ink);
    font-size: 19px;
    font-weight: 400;
    letter-spacing: 0.12em;
    line-height: 1.2;
  }
  .contact__title { margin-bottom: 10px; }
  .contact__business { margin-bottom: 10px; }
  .contact__row { display: flex; gap: 14px; }
  .contact__row + .contact__row { margin-top: 22px; }
  .contact__icons { display: flex; flex-direction: column; width: 14px; }
  .contact__icons svg { width: 11px; height: 11px; margin: 3px 0 3.5px; fill: var(--ink); }
</style>
</head>
<body>
  <section class="card card--front">
    <div class="front-band"></div>
    <p class="brand">Brightbins</p>
  </section>

  <section class="card card--back">
    <p class="brand">Brightbins</p>
    <div class="divider"></div>
    <div class="contact">
      <p class="contact__name">ALAN REED</p>
      <p class="contact__title">Managing Director</p>
      <p class="contact__business">Business</p>
      <div class="contact__row">
        <div class="contact__icons">
          <svg viewBox="0 0 12 12" aria-hidden="true"><path d="M6 1 L11.5 6 H10 V11 H7 V8 H5 V11 H2 V6 H0.5 Z"/></svg>
        </div>
        <div>
          <p>Address Line 1</p>
          <p>Address Line 2</p>
          <p>Address Line 3</p>
        </div>
      </div>
      <div class="contact__row">
        <div class="contact__icons">
          <svg viewBox="0 0 12 12" aria-hidden="true"><path d="M2 1 L4.5 1 L5.5 3.8 L4 5 Q5 7.2 7 8 L8.2 6.5 L11 7.5 L11 10 Q6 11.5 2.5 7.5 Q0.5 4.5 2 1 Z"/></svg>
          <svg viewBox="0 0 12 12" aria-hidden="true"><path d="M3.5 0.5 H8.5 V11.5 H3.5 Z M4.5 1.5 V9 H7.5 V1.5 Z"/></svg>
          <svg viewBox="0 0 12 12" aria-hidden="true"><path d="M0.5 2.5 H11.5 V9.5 H0.5 Z M1.5 3.3 L6 6.6 L10.5 3.3 Z"/></svg>
        </div>
        <div>
          <p>+120 555 0148</p>
          <p>+9870 555 032</p>
          <p>alanreed@mail.com</p>
        </div>
      </div>
    </div>
  </section>
</body>
</html>
```